Name of company is Raven Crest Shear Sharpening and Sales.Card design basic idea; I'm thinking back side just showing a sharp RAVEN CREST. Front side: I'm thinking a tiger showing teeth and claws.With the words "Raven Crest" larger type emphasized on one line.Then "Shear Sharpening and Sales" on the next line.Other info on front of card should be my name and phone #'s and address: Martin Kessling P (555)014-2287 CP (555)017-3365 My address is NOT to be emphasized.Can go at bottom of card. It is: 5072 Henley Court Orlando FL 30417 If all that's too much to fit without looking cluttered than maybe the claw on the front with all the contact info. and just the Tiger on back of card. Whichever looks best.

Target Market(s)

Beauty Salons

Industry/Entity Type

It Company

Contact Information for Business Card

The 2 images,the claw and the tiger,could be either illustrations or photos.Whatever looks best.Got to be eye grabbing either way.

Requirements
Must have
• Contact info. Must be in color. And emphasize the identity. RAVEN CREST.Tiger on one side.Showing TEETH. Raven Crest on the other side. Showing the CLAW. .Both pics must emphasize SHARPNESS...This is a shear SHARPENING business. If one of the claw pics shows cutting grooves into something that's fine too. Card must show sharpness of the claw blade somehow.
Nice to have
• Attention grabbing. Images should jump off the card!
Should not have
• No boring cuddly tiger pics showing no teeth or claws or dull teeth or claws. No Black and whites.. No extra words other than what I've listed.

```html
<!DOCTYPE html>
<html lang="en">
<head>
<meta charset="utf-8">
<title>Raven Crest Business Card</title>
<link rel="stylesheet" href="https://fonts.googleapis.com/css2?family=Poppins:wght@500;600&family=Oswald:wght@600&family=Work+Sans:wght@400&display=swap">
<style>
  :root {
    --page-bg: #2a2a2c;
    --card-blue: #3a53a4;
    --claw-orange: #e0661f;
    --tiger-orange: #e79a3a;
    --tiger-cream: #e9e2d2;
    --ink-white: #ffffff;
  }
  * { margin: 0; padding: 0; box-sizing: border-box; }
  html, body {
    width: 1200px; height: 900px; overflow: hidden;
    background: var(--page-bg);
  }
  .canvas { position: relative; width: 1200px; height: 900px; }
  .card {
    position: absolute; left: 285px; width: 630px; height: 360px;
    background: var(--card-blue); overflow: hidden;
    color: var(--ink-white);
  }
  .card--front { top: 60px; }
  .card--back { top: 480px; }

  /* Front */
  .brand { position: absolute; left: 62px; top: 176px; }
  .brand__name {
    font-family: "Poppins", sans-serif; font-weight: 600;
    font-size: 31px; letter-spacing: 2px; line-height: 1;
    white-space: nowrap;
  }
  .brand__tagline {
    font-family: "Poppins", sans-serif; font-weight: 500;
    font-size: 13px; letter-spacing: 1.2px; margin-top: 6px;
    white-space: nowrap;
  }
  .tiger-art {
    position: absolute; right: 22px; top: 20px; width: 262px; height: 322px;
    border-radius: 46% 46% 40% 40%;
    background: radial-gradient(ellipse at 50% 42%, var(--tiger-orange) 0%, var(--tiger-cream) 58%, rgba(233,226,210,0) 74%);
  }

  /* Back */
  .claw-art {
    position: absolute; left: 0; top: 0; width: 240px; height: 190px;
    background: radial-gradient(ellipse at 35% 35%, var(--claw-orange) 0%, rgba(224,102,31,0.55) 45%, rgba(224,102,31,0) 75%);
  }
  .person {
    position: absolute; left: 150px; top: 190px; width: 270px; text-align: right;
  }
  .person__name {
    font-family: "Oswald", sans-serif; font-weight: 600;
    font-size: 30px; letter-spacing: 1px; line-height: 1.05;
    white-space: nowrap;
  }
  .person__role {
    font-family: "Poppins", sans-serif; font-weight: 500;
    font-size: 18px; letter-spacing: 1.5px;
  }
  .divider {
    position: absolute; left: 440px; top: 196px; width: 2px; height: 70px;
    background: var(--ink-white);
  }
  .phones {
    position: absolute; left: 462px; top: 206px; list-style: none;
    font-family: "Work Sans", sans-serif; font-size: 15px; letter-spacing: 1.5px;
  }
  .phones li { display: flex; align-items: center; gap: 12px; height: 24px; white-space: nowrap; }
  .address {
    position: absolute; left: 200px; top: 316px; display: flex; align-items: center; gap: 12px;
    font-family: "Work Sans", sans-serif; font-size: 15px; letter-spacing: 1.5px;
    white-space: nowrap;
  }
</style>
</head>
<body>
<main class="canvas">

  <section class="card card--front">
    <div class="brand">
      <h1 class="brand__name">RAVEN CREST</h1>
      <p class="brand__tagline">Shear Sharpening and Sales</p>
    </div>
    <div class="tiger-art" role="img" aria-label="Illustration of a roaring tiger head showing sharp fangs"></div>
  </section>

  <section class="card card--back">
    <div class="claw-art" role="img" aria-label="Illustration of four orange claw scratch marks torn into the card"></div>

    <div class="person">
      <h2 class="person__name">MARTIN KESSLING</h2>
      <p class="person__role">Founder</p>
    </div>
    <div class="divider"></div>
    <ul class="phones">
      <li>
        <svg width="14" height="14" viewBox="0 0 24 24" aria-hidden="true"><path fill="#fff" d="M6.6 10.8a15 15 0 0 0 6.6 6.6l2.2-2.2a1 1 0 0 1 1-.25 11.4 11.4 0 0 0 3.6.57 1 1 0 0 1 1 1V20a1 1 0 0 1-1 1A17 17 0 0 1 3 4a1 1 0 0 1 1-1h3.5a1 1 0 0 1 1 1c0 1.250.2 2.45.57 3.6a1 1 0 0 1-.25 1z"/></svg>
        <span>(555)014-2287</span>
      </li>
      <li>
        <svg width="14" height="16" viewBox="0 0 14 20" aria-hidden="true"><rect x="1" y="1" width="12" height="18" rx="2" fill="none" stroke="#fff" stroke-width="1.8"/><circle cx="7" cy="16" r="1" fill="#fff"/></svg>
        <span>(555)017-3365</span>
      </li>
    </ul>
    <p class="address">
      <svg width="12" height="16" viewBox="0 0 12 16" aria-hidden="true"><path fill="#fff" d="M6 0a6 6 0 0 0-6 6c0 4.5 6 10 6 10s6-5.5 6-10a6 6 0 0 0-6-6zm0 8.2A2.2 2.2 0 1 1 6 3.8a2.2 2.2 0 0 1 0 4.4z"/></svg>
      <span>5072 Henley Court Orlando FL 30417</span>
    </p>
  </section>

</main>
</body>
</html>
```